Banner for real estate email blast

I need a banner created that will be used in a commercial real estate broadcast email headed. The banner size should be 800x129 pixels and in a JPG format. I will include our company logo and samples of some other company documents.
The banner MUST include (1) the company name, Holloway-Brisk Real Estate and (2) the following contact information:
472 Tindale Orchard Rd
Fayetteville, NC 28917
(910) 555-0143
www.HollowayBriskRE.example
Target Market(s)
Real estate agents.
Industry/Entity Type
Real Estate
Requirements
Must have
- 1. Company name
- 2. Contact info to include address, phone number, web address
- 3. Use the same green colors as in our other attached documents.
- 4. MUST be 800x129 pixels
Should not have
- Any other text other than what is mentioned in the "Must Haves"

```html
<!DOCTYPE html>
<html lang="en">
<head>
<meta charset="utf-8">
<title>Holloway-Brisk Real Estate – Email Banner</title>
<link rel="stylesheet" href="https://fonts.googleapis.com/css2?family=EB+Garamond:wght@400;500&display=swap">
<style>
  :root {
    --brand-green: #0b6e1c;
    --leaf-soft: #cfe3cc;
    --paper: #ffffff;
    --stage: #e8ece8;
    --text-light: #ffffff;
  }
  html, body {
    margin: 0;
    padding: 0;
    width: 1200px;
    height: 800px;
    overflow: hidden;
    background: var(--stage);
  }
  .banner {
    position: absolute;
    left: 40px;
    top: 287px;
    width: 1120px;
    height: 225px;
    background: var(--paper);
    overflow: hidden;
    font-family: "EB Garamond", Georgia, serif;
    font-variant-numeric: lining-nums;
    box-shadow: 0 2px 8px rgba(0,0,0,0.12);
  }
  .banner__art {
    position: absolute;
    left: 0;
    top: 0;
    width: 1120px;
    height: 225px;
  }
  .banner__contact {
    position: absolute;
    left: 20px;
    top: 182px;
    margin: 0;
    font-size: 20.5px;
    font-weight: 500;
    line-height: 1;
    color: var(--text-light);
    white-space: nowrap;
  }
  .brand__mark {
    position: absolute;
    left: 754px;
    top: 86px;
    width: 72px;
    height: 72px;
    border-radius: 50%;
    background: var(--brand-green);
  }
  .brand__name {
    position: absolute;
    left: 834px;
    top: 80px;
    width: 258px;
    margin: 0;
    color: var(--brand-green);
    font-weight: 400;
    line-height: 1;
    text-align: center;
  }
  .brand__name-main {
    display: block;
    font-size: 41px;
    white-space: nowrap;
  }
  .brand__name-sub {
    display: block;
    font-size: 21px;
    letter-spacing: 5px;
    margin-top: 6px;
    padding-left: 5px;
  }
  .banner__rule {
    position: absolute;
    left: 839px;
    top: 174px;
    width: 242px;
    height: 1px;
    background: var(--brand-green);
  }
  .banner__web {
    position: absolute;
    left: 830px;
    top: 184px;
    width: 260px;
    margin: 0;
    text-align: center;
    font-size: 17.5px;
    font-weight: 500;
    line-height: 1;
    color: var(--brand-green);
    white-space: nowrap;
  }
</style>
</head>
<body>
  <section class="banner">
    <svg class="banner__art" viewBox="0 0 1120 225" role="img" aria-label="Green city skyline silhouette of office towers">
      <defs>
        <linearGradient id="skyline-fill" x1="0" y1="0" x2="0" y2="1">
          <stop offset="0" stop-color="#f3f7f2"/>
          <stop offset="0.3" stop-color="#9cc49e"/>
          <stop offset="0.75" stop-color="#0b6e1c"/>
          <stop offset="1" stop-color="#0b6e1c"/>
        </linearGradient>
      </defs>
      <path d="M0 0 H634 V150 C626 172 618 196 614 225 H0 Z" fill="url(#skyline-fill)"/>
    </svg>

    <svg class="banner__art" viewBox="0 0 1120 225" role="img" aria-label="Sweeping green leaf vine curling up from the skyline">
      <defs>
        <radialGradient id="leaf-fill" cx="640" cy="170" r="240" gradientUnits="userSpaceOnUse">
          <stop offset="0" stop-color="#0b6e1c" stop-opacity="0.9"/>
          <stop offset="0.45" stop-color="#8cbb8f" stop-opacity="0.55"/>
          <stop offset="1" stop-color="#cfe3cc" stop-opacity="0"/>
        </radialGradient>
      </defs>
      <path d="M634 150 C650 80 720 20 800 8 C850 2 890 20 912 60 C860 40 800 50 750 80 C700 110 665 140 634 178 Z" fill="url(#leaf-fill)"/>
    </svg>

    <p class="banner__contact">(910) 555-0143 &nbsp;|&nbsp; 472 Tindale Orchard Rd, Fayetteville, NC 28917</p>

    <span class="brand__mark" aria-hidden="true"></span>
    <h1 class="brand__name">
      <span class="brand__name-main">Holloway-Brisk</span>
      <span class="brand__name-sub">REAL ESTATE</span>
    </h1>
    <div class="banner__rule"></div>
    <p class="banner__web">www.HollowayBriskRE.example</p>
  </section>
</body>
</html>
```